Create a Brochure Design for Brantley Homecare

Brantley Homecare is a subsidiary of the Brantley Care Group. This brochure is specifically for the Brantley Homecare company and brand. Create a 3 panel, A4, front and back, tri-fold brochure. This brochure will be a way to introduce our Homecare services to the community, prospective clients, and various referral partners. The brochure must be eye catching, unique in its deliverables and demonstrate both attention to detail and comfort. Our organization is sophisticated and built around warmth, care and individualized personal attention. The most important aspect of this design is to focus on creating a nurturing, warm, and inviting feel where you would want to have a Nurse or Nurse’s Aide in your own home or a loved one’s home.

I am open to the creativity of the designer to develop something based on the above criteria; however I would like the design to work well with the existing collateral material. What I mean by that is that while I want everything to have its own personality and stand out as its own brand representative, I still need to be able to tell that the overall design concept stays stylistically inside of the same ‘family’ of existing designed material. Because of this, below I would like for the designer to pull inspiration from the link to our website (Located below) as well as from the attachment of our recently refreshed business cards (Attached). This should allow each design to be unique and creative, while still staying inside of a framework and the feel/style that I am looking for.

Finally, I want all the designers to understand that this brochure design is for a private, in home, healthcare company where we are responsible for providing personalized care for a culturally and ethnically diverse make-up clientele of all ages. The photos that are used must represent an image of warmth, care, and a positive interaction between client and caregiver.

Look under the Brantley Homecare tab at www.brantleycaregroup-example.net

Industry/Entity Type

Healthcare

Requirements
Must have
• • The Brantley Homecare company logo must be included.

```html
<!DOCTYPE html>
<html lang="en">
<head>
<meta charset="utf-8">
<title>Brantley Homecare Tri-fold Brochure</title>
<link href="https://fonts.googleapis.com/css2?family=Arimo:wght@400;700&family=Tinos:ital,wght@0,400;1,400;1,700&display=swap" rel="stylesheet">
<style>
:root{
  --teal:#0c7a6d;
  --teal-deep:#0a6a5f;
  --teal-mid:#3e9488;
  --teal-pale:#a9cfc8;
  --mint:#d6e9e5;
  --ink-dark:#0d4d45;
  --white:#ffffff;
  --page:#ffffff;
}
*{margin:0;padding:0;box-sizing:border-box}
html,body{width:1200px;height:1000px;overflow:hidden;background:var(--page)}
.canvas{position:relative;width:1200px;height:1000px}
.sheet{position:absolute;left:254px;width:691px;overflow:hidden}
.sheet--inside{top:0;height:497px}
.sheet--outside{top:502px;height:498px}
.sheet svg.backdrop{position:absolute;inset:0;width:100%;height:100%}
.photo{position:absolute;border-radius:6px;box-shadow:0 0 12px 6px rgba(255,255,255,.55)}
.abs{position:absolute;color:var(--white)}
.heading{font-family:"Arimo",Arial,sans-serif;font-weight:400;text-align:center;line-height:1.15}
.body{font-family:"Tinos","Times New Roman",serif;font-size:10.6px;line-height:1.2}
.body p{text-indent:28px;margin-bottom:12px}
.justify{text-align:justify}
.center{text-align:center}
.quote{font-family:"Tinos","Times New Roman",serif;font-style:italic;font-weight:700;font-size:10.6px;color:var(--ink-dark);text-align:center;line-height:1.3}
.brand{font-family:"Tinos","Times New Roman",serif;text-align:center;display:flex;align-items:center;justify-content:center;gap:8px}
.brand-mark{width:14px;height:14px;display:inline-block}
.tagline{font-family:"Tinos","Times New Roman",serif;font-style:italic;text-align:center;line-height:1.1}
.contact{font-family:"Arimo",Arial,sans-serif;text-align:center;font-size:15.5px;line-height:1.13}
</style>
</head>
<body>
<div class="canvas">

  <section class="sheet sheet--inside">
    <svg class="backdrop" viewBox="0 0 691 497" preserveAspectRatio="none" aria-hidden="true">
      <defs>
        <linearGradient id="insideBase" x1="0" y1="0" x2="1" y2="1">
          <stop offset="0" stop-color="#5aa499"/>
          <stop offset="0.55" stop-color="#2f8a7e"/>
          <stop offset="1" stop-color="#0c7a6d"/>
        </linearGradient>
        <linearGradient id="leftFade" x1="0" y1="0" x2="0" y2="1">
          <stop offset="0" stop-color="#7fb8ae"/>
          <stop offset="1" stop-color="#e4f0ed"/>
        </linearGradient>
        <linearGradient id="rightBand" x1="0" y1="0" x2="1" y2="0">
          <stop offset="0" stop-color="#0c7a6d"/>
          <stop offset="1" stop-color="#6fb2a7"/>
        </linearGradient>
      </defs>
      <rect width="691" height="497" fill="url(#insideBase)"/>
      <path d="M0 300 C 60 380 150 450 300 497 L0 497 Z" fill="url(#leftFade)"/>
      <path d="M470 0 C 640 40 690 150 691 260 L691 497 L560 497 C 650 380 660 220 600 110 C 570 60 520 20 470 0 Z" fill="url(#rightBand)" opacity="0.85"/>
      <path d="M480 0 C 600 30 660 90 691 150 L691 0 Z" fill="var(--white)"/>
    </svg>
    <div role="img" aria-label="Soft-focus garden foliage background photograph" style="position:absolute;left:0;top:0;width:480px;height:300px;background:radial-gradient(ellipse at 40% 35%,rgba(150,200,190,.7),rgba(90,160,150,0) 70%)"></div>
  </section>

  <div class="photo" role="img" aria-label="Portrait photograph of a smiling nurse with a stethoscope" style="left:544px;top:182px;width:113px;height:148px;background:linear-gradient(160deg,#e4e4e4,#9a9a9a)"></div>
  <div class="photo" role="img" aria-label="Photograph of a caregiver sitting with an elderly client at a table" style="left:745px;top:115px;width:152px;height:150px;background:linear-gradient(150deg,#eeeeee,#8c8c8c)"></div>

  <h2 class="abs heading" style="left:280px;top:183px;width:196px;font-size:18.5px">The Brantley Homecare Promise</h2>
  <div class="abs body" style="left:282px;top:237px;width:195px">
    <p>Brantley Homecare is a home health agency located in Honolulu, Hawaii. We provide in-home services ranging from light housekeeping to skilled nursing services. We focus on providing the highest level of quality home care while offering the best value to our clients.</p>
    <p>The Brantley Way is special; it is compassionate, professional, dependable, flexible and is built on the strongest foundation. Everything we do is focused on meeting the individual needs of our clients.</p>
  </div>
  <div class="abs body justify" style="left:507px;top:355px;width:189px">
    <p>Whether you need skilled nursing care, a home assistant, a nurse aide or transportation services, Brantley Homecare can assist with your needs. We also provide care management services, so your home care is planned and managed by experienced, licensed Nurses. We are located in Honolulu, Hawaii, serving the island of Oahu.</p>
  </div>
  <div class="abs body justify" style="left:725px;top:292px;width:193px">
    <p>The Brantley Support Team is available for all of our clients and employees 24 hours a day. Every day of the year. That's one of many reasons why you can depend on us. Another is simple value. We think you'll find our rates are more than competitive. Rates vary based on the level of care needed.</p>
    <p class="center" style="text-indent:0">Please call us for more specific rate information at (808) 555-0147.</p>
  </div>

  <section class="sheet sheet--outside">
    <svg class="backdrop" viewBox="0 0 691 498" preserveAspectRatio="none" aria-hidden="true">
      <defs>
        <linearGradient id="swooshLeft" x1="0" y1="0" x2="1" y2="1">
          <stop offset="0" stop-color="#0c7a6d"/>
          <stop offset="1" stop-color="#d9ebe7"/>
        </linearGradient>
        <linearGradient id="cornerRight" x1="0" y1="0" x2="1" y2="1">
          <stop offset="0" stop-color="#2f8a7e"/>
          <stop offset="1" stop-color="#c9e2dd"/>
        </linearGradient>
      </defs>
      <rect width="691" height="498" fill="var(--teal)"/>
      <path d="M0 280 C 20 390 90 460 160 498 L0 498 Z" fill="url(#swooshLeft)"/>
      <path d="M500 0 C 620 50 680 130 691 190 L691 0 Z" fill="url(#cornerRight)"/>
    </svg>
  </section>

  <div class="photo" role="img" aria-label="Photograph of a caregiver helping a client at home" style="left:727px;top:768px;width:186px;height:122px;background:linear-gradient(150deg,#e8e8e8,#8a8a8a)"></div>

  <h2 class="abs heading" style="left:284px;top:556px;width:188px;font-size:21px">The Brantley Story</h2>
  <p class="abs quote" style="left:284px;top:607px;width:192px">The time will come when we will all have to reach out for help.</p>
  <div class="abs body justify" style="left:281px;top:661px;width:195px">
    <p>It might happen after a sudden, unexpected visit to the hospital. Or it could occur after 70 years where you "never had a single sick day in your life."</p>
    <p>When you reach out, Brantley Homecare will be there. Brantley is more than a home care provider. We're somebody you can depend on without question.</p>
  </div>

  <div class="abs brand" style="left:500px;top:590px;width:200px;color:var(--ink-dark);font-size:24px">
    <span class="brand-mark" style="background:var(--ink-dark)"></span>Brantley Homecare
  </div>
  <p class="abs tagline" style="left:520px;top:660px;width:160px;font-size:10px;color:var(--ink-dark)">Someone you can depend on...<br>Without question.</p>

  <h3 class="abs heading" style="left:520px;top:734px;width:160px;font-size:18px;font-weight:700">Contact Us</h3>
  <div class="abs contact" style="left:490px;top:767px;width:220px">
    <p>Brantley Homecare</p>
    <p>4750 Makana Park Blvd.</p>
    <p>Suite #310</p>
    <p>Honolulu, HI &nbsp; 96800</p>
    <p style="margin-top:17px">Phone: 808-555-0147</p>
    <p>Fax: 808-555-0193</p>
    <p style="margin-top:15px;font-size:15px">info@brantleycare-example.com</p>
  </div>

  <div class="abs brand" style="left:720px;top:680px;width:210px;color:var(--white);font-size:26px">
    <span class="brand-mark" style="background:var(--white)"></span>Brantley Homecare
  </div>
  <p class="abs tagline" style="left:715px;top:913px;width:215px;font-size:16px">Someone you can depend on...<br>Without question.</p>

</div>
</body>
</html>
```